Business Card and Simple Logo Desgin

New Zealand based start up company "Brava Advisory LTD" requires business cards and simple logo design.

Card Content.

Brava Advisory LTD

Rosalind Kettering
CA, BMS (Hons)

r.kettering@bravaadvisory.example.nz
PH +64 21 705 146

Target Market(s)

Corporate Business in IT, Finance and accounting.

Industry/Entity Type

Business

```html
<!DOCTYPE html>
<html lang="en">
<head>
<meta charset="utf-8">
<title>Brava Advisory LTD – Business Card</title>
<link rel="stylesheet" href="https://fonts.googleapis.com/css2?family=Arimo:wght@700&family=Roboto+Condensed:wght@700&display=swap">
<style>
  :root {
    --cyan: #00ccff;
    --cyan-text: #19c8f0;
    --front-top: #e3fdff;
    --front-bottom: #bff6fb;
    --back-edge: #9ef8fc;
    --back-centre: #f4ffff;
    --white: #ffffff;
  }
  * { margin: 0; padding: 0; box-sizing: border-box; }
  html, body {
    width: 908px; height: 1200px; overflow: hidden;
    background: var(--white);
  }
  .canvas { position: relative; width: 908px; height: 1200px; }

  .card {
    position: absolute;
    border-radius: 34px;
    overflow: hidden;
  }

  /* Front */
  .card--front {
    left: 0; top: 0; width: 902px; height: 562px;
    background: linear-gradient(180deg, var(--front-top) 0%, var(--front-bottom) 76%);
  }
  .wordmark {
    font-family: "Arimo", Arial, sans-serif;
    font-weight: 700;
    color: var(--cyan-text);
    line-height: 1;
    position: absolute;
  }
  .card--front .wordmark {
    left: 31px; top: 92px;
  }
  .wordmark__main { display: block; font-size: 64px; letter-spacing: 1px; }
  .wordmark__sub { display: block; font-size: 30px; margin-top: 8px; }

  .holder {
    position: absolute;
    right: 26px; top: 262px;
    text-align: right;
    font-family: "Arimo", Arial, sans-serif;
    font-weight: 700;
    color: var(--cyan-text);
    line-height: 1;
  }
  .holder__name { font-size: 40px; letter-spacing: 4px; }
  .holder__credentials { font-size: 27px; letter-spacing: 2.5px; margin-top: 4px; }

  .contact-band {
    position: absolute;
    left: 0; right: 0; top: 429px; bottom: 0;
    background: linear-gradient(180deg, #45dcff 0%, var(--cyan) 18%, var(--cyan) 100%);
    display: flex; flex-direction: column; align-items: center; justify-content: center;
    font-family: "Roboto Condensed", "Arial Narrow", sans-serif;
    font-weight: 700;
    color: var(--white);
    line-height: 1.05;
  }
  .contact-band__email { font-size: 34px; }
  .contact-band__phone { font-size: 34px; }

  /* Back */
  .card--back {
    left: 8px; top: 638px; width: 894px; height: 559px;
    background: radial-gradient(ellipse 60% 55% at 50% 45%, var(--back-centre) 0%, #c6fbfd 55%, var(--back-edge) 100%);
  }
  .card--back .wordmark {
    left: 0; right: 0; top: 150px;
    text-align: center;
  }
  .card--back .wordmark__main { font-size: 120px; letter-spacing: 2px; }
  .card--back .wordmark__sub { font-size: 58px; margin-top: 20px; }
</style>
</head>
<body>
<main class="canvas">
  <section class="card card--front" aria-label="Business card front">
    <div class="wordmark">
      <span class="wordmark__main">Brava</span>
      <span class="wordmark__sub">Advisory LTD</span>
    </div>
    <div class="holder">
      <p class="holder__name">Rosalind Kettering</p>
      <p class="holder__credentials">CA, BMS (Hons)</p>
    </div>
    <div class="contact-band">
      <p class="contact-band__email">r.kettering@bravaadvisory.example.nz</p>
      <p class="contact-band__phone">PH +64 21 705 146</p>
    </div>
  </section>

  <section class="card card--back" aria-label="Business card back">
    <div class="wordmark">
      <span class="wordmark__main">Brava</span>
      <span class="wordmark__sub">Advisory LTD</span>
    </div>
  </section>
</main>
</body>
</html>
```